Marcus T Orwell DDS (dentist) needs a business card/business logo design

I would like an eye-catchingly conservative or elegant graphic presentation of my business name with the elements: prevention, restoration, and cosmetics (these are the services I'd like to emphasize) .
The business card would have room for address lines, phone and fax, web address. No standard teeth or oral representations please. Should communicate professionalism. Whatever color scheme works.

Thank you

Target Market(s)

I just want a good looking business card

Industry/Entity Type

Conservative

Contact Information for Business Card

Adress: 4716 Wrenfield Ave Lakewood CA 90642 Phone: 562 413 9082 FAX 562 413 5527 Web: Fairbrookdental.example

Font styles to use
Sans Serif

Colors
0255a3

Requirements
Must have
• business name with the elements: prevention, restoration, and cosmetics (these are the services I'd like to emphasize)
• communicates professionalism
Nice to have
• eye catching but not flashy graphics
Should not have
• no pictures of teeth or dental instruments

```html
<!DOCTYPE html>
<html lang="en">
<head>
<meta charset="utf-8">
<title>Marcus T Orwell DDS – Business Card</title>
<link rel="stylesheet" href="https://fonts.googleapis.com/css2?family=PT+Sans:wght@400;700&display=swap">
<style>
  :root {
    --brand-blue: #0255a3;
    --band-black: #000000;
    --accent-yellow: #d6d30a;
    --ink: #0b0b0b;
    --white: #ffffff;
    --stage-light: #ffffff;
    --stage-dark: #e4e4e4;
    --stage-edge: #3a3a3a;
  }
  html, body {
    margin: 0;
    padding: 0;
    width: 1200px;
    height: 1001px;
    overflow: hidden;
  }
  body {
    font-family: "PT Sans", Arial, sans-serif;
  }
  .stage {
    position: relative;
    width: 1200px;
    height: 1001px;
    box-sizing: border-box;
    border: 2px solid var(--stage-edge);
    background: radial-gradient(ellipse at 50% 35%, var(--stage-light) 0%, var(--stage-light) 25%, var(--stage-dark) 100%);
  }
  .card {
    position: absolute;
    left: 276px;
    top: 319px;
    width: 654px;
    height: 363px;
    border-radius: 32px;
    background: var(--brand-blue);
    overflow: hidden;
  }
  .card__divider {
    position: absolute;
    left: 342px;
    top: 0;
    width: 3px;
    height: 106px;
    background: var(--white);
  }
  .identity {
    position: absolute;
    right: 26px;
    top: 48px;
    max-width: 270px;
    text-align: right;
  }
  .identity__name {
    margin: 0;
    font-weight: 700;
    font-size: 29px;
    line-height: 1;
    color: var(--ink);
    letter-spacing: -0.3px;
    white-space: nowrap;
  }
  .identity__role {
    margin: 6px 6px 0 0;
    font-weight: 700;
    font-size: 21px;
    line-height: 1;
    color: var(--white);
  }
  .contact {
    position: absolute;
    left: 0;
    top: 0;
    margin: 0;
    padding: 0;
    list-style: none;
  }
  .contact__item {
    position: absolute;
    left: 48px;
    display: flex;
    align-items: flex-start;
    gap: 14px;
    font-size: 19.5px;
    line-height: 21px;
    color: var(--ink);
    white-space: nowrap;
  }
  .contact__item--address { top: 45px; }
  .contact__item--phone { top: 105px; }
  .contact__item--fax { top: 155px; }
  .contact__item--web { top: 201px; }
  .contact__icon {
    width: 26px;
    height: 24px;
    flex: none;
  }
  .contact__item--address .contact__text { margin-left: 4px; margin-top: -3px; }
  .tagline-band {
    position: absolute;
    left: 0;
    top: 254px;
    width: 100%;
    height: 68px;
    background: var(--band-black);
    border-bottom: 5px solid var(--accent-yellow);
  }
  .tagline-band__text {
    position: absolute;
    left: 38px;
    top: 18px;
    margin: 0;
    font-size: 29px;
    line-height: 1;
    letter-spacing: 2.85px;
    word-spacing: 5px;
    color: var(--white);
    white-space: nowrap;
  }
</style>
</head>
<body>
<main class="stage">
  <section class="card" aria-label="Business card for Marcus T Orwell DDS">
    <div class="card__divider"></div>

    <header class="identity">
      <h1 class="identity__name">Marcus T Orwell DDS</h1>
      <p class="identity__role">dentist</p>
    </header>

    <ul class="contact">
      <li class="contact__item contact__item--address">
        <svg class="contact__icon" viewBox="0 0 26 24" aria-hidden="true">
          <path d="M13 2 L1 12.5 L3.2 12.5 L13 4.2 L22.8 12.5 L25 12.5 Z" fill="#fff"/>
          <path d="M5 12.5 L13 6 L21 12.5 V23 H15.5 V16.5 H10.5 V23 H5 Z" fill="#fff"/>
          <rect x="18.5" y="3" width="2.6" height="5" fill="#fff"/>
        </svg>
        <span class="contact__text">4716 Wrenfield<br>Ave Lakewood CA 90642</span>
      </li>
      <li class="contact__item contact__item--phone">
        <svg class="contact__icon" viewBox="0 0 26 26" aria-hidden="true">
          <path d="M7 2 C4 3 3 6 4.5 10 C6.5 15.5 10 20 15 23.5 C18 25.5 20.5 24.5 22 22.5 L18.5 18.5 C17.5 19.2 16.5 19.6 15.5 18.8 C12.5 16.3 10.5 13 9.4 10 C9 8.8 9.6 8 10.6 7.4 Z" fill="#fff"/>
        </svg>
        <span class="contact__text">562 413 9082</span>
      </li>
      <li class="contact__item contact__item--fax">
        <svg class="contact__icon" viewBox="0 0 26 24" aria-hidden="true">
          <rect x="7" y="1" width="12" height="8" fill="#fff"/>
          <rect x="1" y="9" width="24" height="10" rx="2" fill="#fff"/>
          <rect x="6" y="15" width="14" height="8" fill="#fff" stroke="#0255a3" stroke-width="1.4"/>
          <rect x="9" y="3.5" width="8" height="1.2" fill="#0255a3"/>
          <rect x="9" y="6" width="8" height="1.2" fill="#0255a3"/>
        </svg>
        <span class="contact__text">562 413 5527</span>
      </li>
      <li class="contact__item contact__item--web">
        <svg class="contact__icon" viewBox="0 0 26 26" aria-hidden="true">
          <g fill="none" stroke="#fff" stroke-width="1.8">
            <circle cx="13" cy="13" r="11"/>
            <ellipse cx="13" cy="13" rx="5" ry="11"/>
            <line x1="13" y1="2" x2="13" y2="24"/>
            <line x1="2" y1="13" x2="24" y2="13"/>
            <path d="M4 7.5 H22 M4 18.5 H22"/>
          </g>
        </svg>
        <span class="contact__text">Fairbrookdental.example</span>
      </li>
    </ul>

    <div class="tagline-band">
      <p class="tagline-band__text">prevention, restoration, and cosmetics</p>
    </div>
  </section>
</main>
</body>
</html>
```